Harlow Ironworks Business Card

We need a business card design for a new small metal fabrication business in rural NSW, Australia.

The business (Harlow Ironworks) is owner operated by a man with the initials KB - much of the branding comes from this name.

Harlow Ironworks designs, engineers, repairs and manufactures a range of custom, quality metal works including vehicle trays, agricultural machinery impliments, trailers, wood splitters, fire pits, furniture etc.

The brand position focuses on custom work of the highest quality.

Business card design should show quality, attention to detail and stand out among a mass of business cards.

Logos are in the files

The grey color may be changed on the logo if required to stand out more.

There is an image attached of a simple card that is liked because it is clean, clear, simple, masculine and effective. It says 'quality'. As most of the work we do is custom it would be good to have the business card speak to this.

Target Market(s)

Rural and regional based Australians. Primarily adult male 25-60 yrs. Primary production / rural / travelling lifestyle.

Industry/Entity Type

Metal Fabrication

Contact Information for Business Card

The words 'custom quality fabrications' would be great somewhere perhaps on the backside (not on the information side)
Name
title
Phone: 0418 539 746 and (02) 6193 4827
email: info@harlowiw.com.au
www.harlowiw.com.au

address (2 lines)

Requirements
Nice to have
• Background colour should be very navy blue or black.
Should not have
• NO orange and blue combinations.
• Navy is OK

```html
<!DOCTYPE html>
<html lang="en">
<head>
<meta charset="utf-8">
<title>Harlow Ironworks Business Card</title>
<link href="https://fonts.googleapis.com/css2?family=Open+Sans:wght@400;600;700&display=swap" rel="stylesheet">
<style>
  :root {
    --stage: #3b3633;
    --card-black: #050505;
    --band-black: #111111;
    --card-white: #ffffff;
    --brand-green: #5bbf3a;
    --brand-grey: #a7a7a7;
    --text-grey: #8a8a8a;
    --name-grey: #7d7d7d;
  }
  * { margin: 0; padding: 0; box-sizing: border-box; }
  html, body {
    width: 1200px; height: 780px; overflow: hidden;
    background: var(--stage);
    font-family: "Open Sans", Arial, sans-serif;
  }
  .stage {
    position: relative; width: 1200px; height: 780px;
    display: flex; align-items: center; justify-content: center; gap: 48px;
  }
  .card {
    width: 520px; height: 318px; position: relative; overflow: hidden;
    box-shadow: 0 14px 30px rgba(0,0,0,0.45);
  }
  /* Front */
  .card-front {
    background: var(--card-black);
    display: flex; flex-direction: column; align-items: center; justify-content: center;
  }
  .brand-lockup { display: flex; align-items: center; gap: 14px; }
  .brand-mark { width: 30px; height: 30px; background: var(--brand-green); flex: none; }
  .brand-name {
    font-weight: 700; font-size: 34px; letter-spacing: 2px;
    color: var(--brand-grey); text-transform: uppercase; white-space: nowrap;
  }
  .front-web {
    margin-top: 26px; font-size: 14px; color: var(--text-grey);
  }
  /* Back */
  .card-back { background: var(--card-white); display: flex; }
  .side-band {
    position: relative; flex: none;
    width: 112px; height: 100%; background: var(--band-black);
  }
  .side-brand {
    position: absolute; left: 50%; top: 50%;
    transform: translate(-50%, -50%) rotate(-90deg);
    white-space: nowrap;
    display: flex; align-items: center; gap: 8px;
  }
  .side-brand .brand-mark { width: 16px; height: 16px; }
  .side-brand .brand-name { font-size: 19px; letter-spacing: 1px; }
  .contact { padding: 64px 0 0 36px; color: var(--text-grey); }
  .person-name {
    font-weight: 700; font-size: 19px; color: var(--name-grey);
    text-transform: uppercase; letter-spacing: 0.5px;
  }
  .person-title { font-size: 15px; color: var(--brand-green); margin-bottom: 10px; }
  .address { font-size: 15px; line-height: 1.35; margin-bottom: 8px; }
  .contact-list { list-style: none; }
  .contact-item {
    display: flex; align-items: center; gap: 10px;
    font-size: 15px; line-height: 1.45;
  }
  .contact-icon { width: 15px; height: 15px; flex: none; }
</style>
</head>
<body>
<main class="stage">
  <section class="card card-front" aria-label="Card front">
    <div class="brand-lockup">
      <span class="brand-mark"></span>
      <span class="brand-name">Harlow Ironworks</span>
    </div>
    <p class="front-web">harlowiw.com.au</p>
  </section>

  <section class="card card-back" aria-label="Card back">
    <div class="side-band">
      <div class="side-brand">
        <span class="brand-mark"></span>
        <span class="brand-name">Harlow Ironworks</span>
      </div>
    </div>
    <div class="contact">
      <p class="person-name">Liam Carter</p>
      <p class="person-title">Director</p>
      <p class="address">PO BOX 418 Gundagai Road<br>Tumut NSW 2720</p>
      <ul class="contact-list">
        <li class="contact-item">
          <svg class="contact-icon" viewBox="0 0 16 16"><rect width="16" height="16" fill="#5bbf3a"/><path d="M4 3h3l1 3-1.5 1a6 6 0 0 0 2.5 2.5L10 8l3 1v3h-2A8 8 0 0 1 4 5z" fill="#fff"/></svg>
          (02) 6193 4827
        </li>
        <li class="contact-item">
          <svg class="contact-icon" viewBox="0 0 16 16"><rect width="16" height="16" fill="#5bbf3a"/><rect x="5" y="2.5" width="6" height="11" rx="1" fill="#fff"/><rect x="6" y="4" width="4" height="7" fill="#5bbf3a"/></svg>
          0418 539 746
        </li>
        <li class="contact-item">
          <svg class="contact-icon" viewBox="0 0 16 16"><rect width="16" height="16" fill="#5bbf3a"/><rect x="3" y="4.5" width="10" height="7" fill="#fff"/><path d="M3 4.5l5 4 5-4" fill="none" stroke="#5bbf3a" stroke-width="1"/></svg>
          info@harlowiw.com.au
        </li>
        <li class="contact-item">
          <svg class="contact-icon" viewBox="0 0 16 16"><rect width="16" height="16" fill="#5bbf3a"/><circle cx="8" cy="8" r="5" fill="none" stroke="#fff" stroke-width="1.2"/><path d="M3 8h10M8 3c-2.5 3-2.5 7 0 10M8 3c2.5 3 2.5 7 0 10" fill="none" stroke="#fff" stroke-width="1"/></svg>
          www.harlowiw.com.au
        </li>
      </ul>
    </div>
  </section>
</main>
</body>
</html>
```